Financial Services Company power point theme design

We need a PowerPoint theme designed for client presentations and company orientations. We do like modern designs using blue colors. attached is our logos the logo colors may change as needed to fit the theme. Landscape 16: 9 is acceptable

Industry/Entity Type

Financial Service

Colors

Designer to choose colors to be used in the design.

```html
<!DOCTYPE html>
<html lang="en">
<head>
<meta charset="utf-8">
<title>Keystone Ridge Financial – Presentation Theme</title>
<link href="https://fonts.googleapis.com/css2?family=Montserrat:wght@400;500;600;700;800&display=swap" rel="stylesheet">
<style>
:root{
  --navy:#13237a;
  --blue:#1f3fae;
  --royal:#2848c0;
  --sky:#4f7ae8;
  --ink:#2a2a2a;
  --text:#555;
  --grey:#c9c9c9;
  --stone:#6f7480;
  --mist:#b9bcc2;
  --coral:#ea5a3d;
  --bg:#000;
}
*{margin:0;padding:0;box-sizing:border-box}
html,body{width:1200px;height:1182px;overflow:hidden;background:var(--bg)}
body{position:relative;font-family:'Montserrat',sans-serif;color:var(--text)}
.slide{position:absolute;width:379px;height:215px;background:#fff;overflow:hidden}
.slide.light::after{content:"";position:absolute;left:0;right:0;bottom:0;height:6px;background:var(--grey)}
.rule{position:absolute;left:10px;top:0;width:150px;height:2px;background:var(--blue)}
.heading{position:absolute;left:10px;top:12px;font-size:13px;font-weight:800;color:var(--ink);letter-spacing:-.2px;text-transform:uppercase;font-family:'Montserrat',sans-serif}
.heading b{color:var(--blue);font-weight:800}
.brand{position:absolute;display:flex;align-items:center;gap:4px;font-weight:600;text-transform:uppercase;line-height:1.1;font-family:'Montserrat',sans-serif}
.brand i{display:block;background:currentColor}
.brand.small{top:8px;right:8px;font-size:4.2px;color:var(--navy);width:70px}
.brand.small i{width:9px;height:9px;flex:none}
.brand.large{font-size:8px;color:#fff;width:150px}
.brand.large i{width:22px;height:22px;flex:none}
.copy{font-size:4.3px;line-height:7.2px;color:var(--text);text-align:justify}
.copy p+p{margin-top:5px}
.subtitle{font-size:9px;font-weight:600;color:var(--blue);position:absolute}
.photo{position:absolute;background:linear-gradient(135deg,#c9d6e8,#8fa4c4 55%,#6a7fa8)}
.photo.warm{background:linear-gradient(135deg,#e9dcc8,#b9a58c 50%,#6d7fa6)}
.photo.desk{background:linear-gradient(150deg,#eef2f6,#c5d1dc 55%,#8d9aa8)}
.blue-slide{background:var(--blue)}
.title-xl{color:#fff;font-weight:700;font-size:17px;letter-spacing:-.2px;text-transform:uppercase;position:absolute}
.lede{color:#e8ecff;font-size:5px;line-height:7.5px;position:absolute}
.coltitle{color:var(--coral);font-weight:600;font-size:7.5px;text-align:center}
.icon-title{color:var(--blue);font-weight:700;font-size:6.8px;text-align:center;text-transform:uppercase;margin:6px 0 4px}
.badge{position:absolute;border-radius:50%;display:flex;flex-direction:column;align-items:center;justify-content:center;color:#fff;text-align:center}
</style>
</head>
<body>

<!-- Row 1 -->
<section class="slide blue-slide" style="left:16px;top:14px">
  <div class="photo" role="img" aria-label="Faded photo of a smiling family outdoors" style="left:150px;top:0;width:229px;height:215px;background:linear-gradient(90deg,rgba(31,63,174,1),rgba(80,110,200,.55));"></div>
  <div style="position:absolute;left:0;right:0;bottom:0;height:6px;background:#2c3f7a"></div>
  <div class="brand large" style="left:22px;top:78px"><i></i><span>Keystone Ridge<br>Financial LLC.</span></div>
  <h1 class="title-xl" style="left:22px;top:106px">Project Title Here</h1>
  <p class="lede" style="left:22px;top:130px;width:185px">Lorem Ipsum is simply dummy text of the printing and typesetting industry. Lorem Ipsum has been the industry's standard dummy text ever since the 1500s.</p>
</section>

<section class="slide light" style="left:404px;top:14px">
  <div class="rule"></div>
  <h2 class="heading">Two <b>Col Content</b></h2>
  <div class="brand small"><i></i><span>Keystone Ridge Financial LLC.</span></div>
  <div class="subtitle" style="left:13px;top:49px">Col Title</div>
  <div class="copy" style="position:absolute;left:13px;top:61px;width:163px">
    <p>Lorem Ipsum is simply dummy text of the printing and typesetting industry. Lorem Ipsum has been the industry's standard dummy text ever since the 1500s, when an unknown printer took a galley of type and scrambled it to make a type specimen book. It has survived not only five centuries, but also the leap into electronic typesetting, remaining essentially unchanged.</p>
    <p>Lorem Ipsum has been the industry's standard dummy text ever since the 1500s, when an unknown printer took a galley of type and scrambled it to make a type specimen book. It has survived not only five centuries, but also the leap into electronic typesetting.</p>
  </div>
  <div class="copy" style="position:absolute;left:192px;top:61px;width:163px">
    <p>Lorem Ipsum is simply dummy text of the printing and typesetting industry. Lorem Ipsum has been the industry's standard dummy text ever since the 1500s, when an unknown printer took a galley of type and scrambled it to make a type specimen book. It has survived not only five centuries, but also the leap into electronic typesetting, remaining essentially unchanged.</p>
    <p>Lorem Ipsum has been the industry's standard dummy text ever since the 1500s, when an unknown printer took a galley of type and scrambled it to make a type specimen book. It has survived not only five centuries, but also the leap into electronic typesetting.</p>
  </div>
  <svg style="position:absolute;right:16px;bottom:0" width="18" height="10"><polygon points="6,0 18,0 12,10 0,10" fill="var(--navy)"/></svg>
</section>

<section class="slide light" style="left:792px;top:14px">
  <div class="rule"></div>
  <h2 class="heading">One <b>Col Content</b></h2>
  <div class="brand small"><i></i><span>Keystone Ridge Financial LLC.</span></div>
  <div class="subtitle" style="left:16px;top:45px">Col Title</div>
  <div class="copy" style="position:absolute;left:16px;top:57px;width:154px">
    <p>Lorem Ipsum is simply dummy text of the printing and typesetting industry. Lorem Ipsum has been the industry's standard dummy text ever since the 1500s, when an unknown printer took a galley of type and scrambled it to make a type specimen book. It has survived not only five centuries, but also the leap into electronic typesetting, remaining essentially unchanged.</p>
    <p>Lorem Ipsum has been the industry's standard dummy text ever since the 1500s, when an unknown printer took a galley of type and scrambled it to make a type specimen book. It has survived not only five centuries, but also the leap into electronic typesetting.</p>
  </div>
  <div style="position:absolute;left:204px;top:54px;width:134px;height:134px;border-radius:50%;border:1.5px solid #c7cdd6"></div>
  <div class="photo desk" role="img" aria-label="Photo of a pen resting on financial documents" style="left:209px;top:59px;width:124px;height:124px;border-radius:50%"></div>
  <div style="position:absolute;left:231px;top:58px;width:11px;height:11px;border-radius:50%;background:#8a8f98"></div>
  <div style="position:absolute;left:311px;top:158px;width:13px;height:13px;border-radius:50%;background:var(--navy)"></div>
  <svg style="position:absolute;right:16px;bottom:0" width="18" height="10"><polygon points="6,0 18,0 12,10 0,10" fill="var(--navy)"/></svg>
</section>

<!-- Row 2 -->
<section class="slide light" style="left:16px;top:244px">
  <div class="rule"></div>
  <h2 class="heading">Our <b>Statics</b></h2>
  <div class="brand small"><i></i><span>Keystone Ridge Financial LLC.</span></div>
  <div style="position:absolute;left:113px;top:52px;width:124px;height:124px;border-radius:50%;border:1px solid #9fb2e6"></div>
  <div class="photo" role="img" aria-label="Photo of a father carrying his daughter on his shoulders" style="left:117px;top:56px;width:116px;height:116px;border-radius:50%"></div>
  <div class="badge" style="left:195px;top:44px;width:42px;height:42px;background:var(--navy);border:2px solid #fff">
    <span style="font-size:10px;font-weight:500">100+</span><span style="font-size:5px">Staff</span>
  </div>
  <div class="badge" style="left:92px;top:138px;width:54px;height:54px;background:var(--sky)">
    <span style="font-size:11px;font-weight:500">1000+</span><span style="font-size:5px">OUR CLients</span>
  </div>
</section>

<section class="slide light" style="left:404px;top:244px">
  <div class="rule"></div>
  <h2 class="heading">3 <b style="color:var(--ink)">Col Content</b></h2>
  <div class="brand small"><i></i><span>Keystone Ridge Financial LLC.</span></div>
  <div class="photo warm" role="img" aria-label="Photo of hands signing a document" style="left:24px;top:55px;width:96px;height:83px;clip-path:polygon(50% 0,100% 100%,0 100%);background:linear-gradient(135deg,#c9a227,#b88a3a 45%,#c5cbd6)"></div>
  <div class="photo warm" role="img" aria-label="Photo of a smiling family" style="left:142px;top:55px;width:96px;height:83px;clip-path:polygon(0 0,100% 0,50% 100%)"></div>
  <div class="photo desk" role="img" aria-label="Photo of a pen on paperwork" style="left:259px;top:55px;width:96px;height:83px;clip-path:polygon(50% 0,100% 100%,0 100%)"></div>
  <div style="position:absolute;left:14px;top:146px;width:352px;display:flex;justify-content:space-between">
    <div style="width:112px"><div class="coltitle">Col Title Text here</div><p class="copy" style="text-align:center;margin-top:3px">Lorem Ipsum is simply dummy text of the printing and typesetting industry. Lorem Ipsum has been the industry's standard dummy text ever since the 1500s.</p></div>
    <div style="width:112px"><div class="coltitle">Col Title Text here</div><p class="copy" style="text-align:center;margin-top:3px">Lorem Ipsum is simply dummy text of the printing and typesetting industry. Lorem Ipsum has been the industry's standard dummy text ever since the 1500s.</p></div>
    <div style="width:112px"><div class="coltitle">Col Title Text here</div><p class="copy" style="text-align:center;margin-top:3px">Lorem Ipsum is simply dummy text of the printing and typesetting industry. Lorem Ipsum has been the industry's standard dummy text ever since the 1500s.</p></div>
  </div>
</section>

<section class="slide light" style="left:792px;top:244px">
  <div class="rule"></div>
  <h2 class="heading">About <b>Introduction</b></h2>
  <div class="brand small"><i></i><span>Keystone Ridge Financial LLC.</span></div>
  <div class="photo warm" role="img" aria-label="Diamond-cropped photos of a business handshake" style="left:0;top:55px;width:148px;height:110px;clip-path:polygon(0 20%,18% 0,36% 20%,55% 0,100% 26%,55% 55%,36% 100%,0 60%);background:linear-gradient(135deg,#c9a227,#d9c9ae 45%,#8e9bb4)"></div>
  <div class="copy" style="position:absolute;left:150px;top:52px;width:210px">
    <p>Lorem Ipsum is simply dummy text of the printing and typesetting industry. Lorem Ipsum has been the industry's standard dummy text ever since the 1500s, when an unknown printer took a galley of type and scrambled it to make a type specimen book. It has survived not only five centuries, but also the leap into electronic typesetting, remaining essentially unchanged. It was popularised in the 1960s with the release of Letraset sheets.</p>
    <p>Lorem Ipsum is simply dummy text of the printing and typesetting industry. Lorem Ipsum has been the industry's standard dummy text ever since the 1500s, when an unknown printer took a galley of type and scrambled it to make a type specimen book.</p>
    <p>It was popularised in the 1960s with the release of Letraset sheets containing Lorem Ipsum passages, and more recently with desktop publishing software.</p>
  </div>
  <div style="position:absolute;right:14px;bottom:0;width:16px;height:10px;background:var(--navy);color:#fff;font-size:5px;font-weight:700;text-align:center;line-height:10px">01</div>
</section>

<!-- Row 3 -->
<section class="slide light" style="left:16px;top:475px">
  <div class="rule" style="width:150px"></div>
  <h2 class="heading">Our <b>Partner</b></h2>
  <div style="position:absolute;left:14px;top:72px;width:150px;display:grid;grid-template-columns:repeat(4,30px);gap:8px 8px">
    <span style="width:24px;height:24px;border-radius:50%;background:#b6b6b6"></span>
    <span style="width:34px;height:22px;border-radius:50%;border:2px solid #9c9c9c"></span>
    <span style="width:24px;height:24px;border-radius:50%;background:#a6a6a6;margin-left:6px"></span>
    <span style="width:24px;height:24px;border-radius:50%;background:#9d9d9d;margin-left:4px"></span>
  </div>
  <div style="position:absolute;left:14px;top:116px;display:flex;gap:8px">
    <span style="width:34px;height:9px;background:#a8a8a8"></span>
    <span style="width:36px;height:9px;background:#bdbdbd"></span>
    <span style="width:28px;height:9px;background:#a8a8a8"></span>
    <span style="width:28px;height:9px;background:#9a9a9a"></span>
  </div>
  <div style="position:absolute;left:40px;top:137px;display:flex;gap:10px">
    <span style="width:26px;height:12px;background:#b4b4b4"></span>
    <span style="width:52px;height:8px;background:#c4c4c4;margin-top:2px"></span>
  </div>
  <div class="copy" style="position:absolute;left:178px;top:50px;width:184px">
    <p>Lorem Ipsum is simply dummy text of the printing and typesetting industry. Lorem Ipsum has been the industry's standard dummy text ever since the 1500s, when an unknown printer took a galley of type and scrambled it to make a type specimen book. It has survived not only five centuries, but also the leap into electronic typesetting, remaining essentially unchanged. It was popularised in the 1960s.</p>
    <p>Lorem Ipsum is simply dummy text of the printing and typesetting industry. Lorem Ipsum has been the industry's standard dummy text ever since the 1500s, when an unknown printer took a galley of type and scrambled it to make a type specimen book. It has survived not only five centuries, remaining essentially unchanged.</p>
  </div>
</section>

<section class="slide light" style="left:404px;top:475px">
  <div class="rule" style="left:0;width:150px"></div>
  <h2 class="heading">Our <b>Graphics</b></h2>
  <svg style="position:absolute;left:80px;top:28px" width="220" height="170" viewBox="0 0 220 170" font-family="Montserrat, sans-serif" text-anchor="middle">
    <polygon points="110,2 150,70 70,70" fill="var(--navy)" stroke="var(--navy)" stroke-width="6" stroke-linejoin="round"/>
    <text x="110" y="46" fill="#fff" font-size="14" font-weight="800">K2</text>
    <text x="110" y="56" fill="#fff" font-size="5.5" font-weight="500">EDUCATION</text>
    <text x="110" y="63" fill="#fff" font-size="5.5" font-weight="500">SYSTEM</text>
    <polygon points="70,78 150,78 110,146" fill="var(--sky)" stroke="var(--sky)" stroke-width="6" stroke-linejoin="round"/>
    <text x="110" y="97" fill="#fff" font-size="13" font-weight="800">200 B</text>
    <text x="110" y="107" fill="#fff" font-size="5.5" font-weight="500">ANNUAL</text>
    <text x="110" y="113" fill="#fff" font-size="5.5" font-weight="500">SPENDING</text>
    <polygon points="39,88 77,152 2,152" fill="var(--stone)" stroke="var(--stone)" stroke-width="6" stroke-linejoin="round"/>
    <text x="40" y="134" fill="#fff" font-size="13" font-weight="800">3M</text>
    <text x="40" y="144" fill="#fff" font-size="5.5" font-weight="500">TEACHER</text>
    <polygon points="180,88 218,152 142,152" fill="var(--mist)" stroke="var(--mist)" stroke-width="6" stroke-linejoin="round"/>
    <text x="178" y="121" fill="#fff" font-size="12" font-weight="800">NO</text>
    <text x="179" y="135" fill="#fff" font-size="12" font-weight="800">COST</text>
    <text x="180" y="145" fill="#fff" font-size="5.5" font-weight="500">CONSULTATION</text>
  </svg>
</section>

<section class="slide light" style="left:792px;top:475px">
  <div class="rule"></div>
  <h2 class="heading">Our <b>Graphics</b></h2>
  <div class="brand small"><i></i><span>Keystone Ridge Financial LLC.</span></div>
  <div style="position:absolute;left:30px;top:68px;width:340px;display:flex;gap:22px">
    <div style="width:96px">
      <svg style="display:block;margin:0 auto" width="30" height="30" viewBox="0 0 30 30" fill="none" stroke="var(--navy)" stroke-width="1.3"><rect x="3" y="2" width="24" height="26"/><line x1="3" y1="8" x2="27" y2="8"/><circle cx="6" cy="5" r=".8"/><circle cx="9" cy="5" r=".8"/><line x1="7" y1="13" x2="20" y2="13"/><line x1="7" y1="17" x2="20" y2="17"/><line x1="7" y1="21" x2="20" y2="21"/><rect x="22" y="12" width="2" height="2"/><rect x="22" y="16" width="2" height="2"/><rect x="22" y="20" width="2" height="2"/></svg>
      <div class="icon-title">Icons Title Here</div>
      <p class="copy">Lorem Ipsum is simply dummy text of the printing and typesetting industry. Lorem Ipsum has been the industry's standard dummy text ever since the 1500s, when an unknown printer took a galley of type and scrambled it to make a type specimen book.</p>
    </div>
    <div style="width:96px">
      <svg style="display:block;margin:0 auto" width="30" height="30" viewBox="0 0 30 30" fill="none" stroke="var(--navy)" stroke-width="1.3"><path d="M9 13V9a6 6 0 0 1 12 0v4"/><rect x="6" y="13" width="18" height="15" rx="2"/><circle cx="15" cy="19" r="2"/><line x1="15" y1="21" x2="15" y2="24"/></svg>
      <div class="icon-title">Icons Title Here</div>
      <p class="copy">Lorem Ipsum is simply dummy text of the printing and typesetting industry. Lorem Ipsum has been the industry's standard dummy text ever since the 1500s, when an unknown printer took a galley of type and scrambled it to make a type specimen book.</p>
    </div>
    <div style="width:96px">
      <svg style="display:block;margin:0 auto" width="30" height="30" viewBox="0 0 30 30" fill="none" stroke="var(--navy)" stroke-width="1.3"><rect x="2" y="3" width="26" height="17"/><polyline points="5,16 10,10 14,13 19,7 25,11"/><line x1="15" y1="20" x2="15" y2="24"/><line x1="15" y1="24" x2="9" y2="29"/><line x1="15" y1="24" x2="21" y2="29"/></svg>
      <div class="icon-title">Icons Title Here</div>
      <p class="copy">Lorem Ipsum is simply dummy text of the printing and typesetting industry. Lorem Ipsum has been the industry's standard dummy text ever since the 1500s, when an unknown printer took a galley of type and scrambled it to make a type specimen book.</p>
    </div>
  </div>
</section>

<!-- Row 4 -->
<section class="slide blue-slide" style="left:16px;top:705px">
  <div class="photo" role="img" aria-label="Faded photo of a hand writing on paperwork" style="left:0;top:0;width:379px;height:215px;background:linear-gradient(120deg,rgba(31,63,174,1) 30%,rgba(60,90,190,.9) 70%,rgba(40,70,180,1))"></div>
  <h1 class="title-xl" style="left:20px;top:96px">Section Title Here</h1>
  <p class="lede" style="left:20px;top:118px;width:220px;font-size:4.3px;line-height:7px">Lorem Ipsum is simply dummy text of the printing and typesetting industry. Lorem Ipsum has been the industry's standard dummy text ever since the 1500s.</p>
</section>

<section class="slide" style="left:407px;top:705px;width:378px">
  <div class="photo warm" role="img" aria-label="Photo of a smiling father with his daughter on his shoulders and a woman beside them" style="left:0;top:0;width:378px;height:215px"></div>
  <svg style="position:absolute;left:0;top:0" width="378" height="215"><polygon points="0,0 126,0 212,215 0,215" fill="var(--blue)"/></svg>
  <div class="brand large" style="left:24px;top:80px"><i></i><span>Keystone Ridge<br>Financial LLC.</span></div>
  <h1 class="title-xl" style="left:24px;top:111px;font-size:10.5px">Project Title Here</h1>
  <p class="lede" style="left:24px;top:126px;width:128px;text-align:justify">Lorem Ipsum is simply dummy text of the printing and typesetting industry. Lorem Ipsum has been the industry's standard dummy text ever since the 1500s.</p>
</section>

<section class="slide" style="left:797px;top:705px;width:384px">
  <div class="photo warm" role="img" aria-label="Photo of a smiling father with his daughter on his shoulders" style="left:0;top:0;width:384px;height:215px"></div>
  <svg style="position:absolute;left:0;top:0" width="384" height="215"><polygon points="128,0 384,0 384,215 208,215" fill="var(--blue)"/></svg>
  <div class="brand large" style="left:190px;top:62px"><i></i><span>Keystone Ridge<br>Financial LLC.</span></div>
  <h1 class="title-xl" style="left:187px;top:100px">Project Title Here</h1>
  <p class="lede" style="left:187px;top:123px;width:185px">Lorem Ipsum is simply dummy text of the printing and typesetting industry. Lorem Ipsum has been the industry's standard dummy text ever since the 1500s.</p>
  <div style="position:absolute;left:0;right:0;bottom:0;height:4px;background:#8a93a6"></div>
</section>

<!-- Row 5 -->
<section class="slide blue-slide" style="left:22px;top:941px;width:385px">
  <div class="photo desk" role="img" aria-label="Photo of a pen lying on financial documents" style="left:236px;top:-30px;width:300px;height:260px;border-radius:50%"></div>
  <div style="position:absolute;left:0;right:0;bottom:0;height:6px;background:#6f7a92"></div>
  <div class="brand large" style="left:24px;top:76px"><i></i><span>Keystone Ridge<br>Financial LLC.</span></div>
  <h1 class="title-xl" style="left:24px;top:108px">Project Title Here</h1>
  <p class="lede" style="left:24px;top:131px;width:185px">Lorem Ipsum is simply dummy text of the printing and typesetting industry. Lorem Ipsum has been the industry's standard dummy text ever since the 1500s.</p>
</section>

</body>
</html>
```